Company profile urgent

Hi, I had my designer fail to deliver and I am looking for urgent designers job. Needs to go to print tomorrow the latest. I need company profile designed and finished, I do have a start of the project but did not like the overall design as it was too simple and not something I would asking for. This needs to be a great job and we are willing to pay for the right job.

This is pretty much a folded brochure as you will see from the document that is attached. On the front side do not remove LOGO from the actual position as it must stay there for the purposes of the cover that is going over and it has a whole for the logo where it is. Also, the pages are set as it should be so do not change the order of the pages, only the design, feel and look. This is for a travel company needs to look expensive, upscale, vip and must have clean design.

Needs to be done:

.

Needs to be done:

1) Get the design more attractive and modern. Not looking for cheap but high quality material.
2) As you can see we are tryin to present 4 products in the brochure that we do and this will be a folded brochure.
3) Infographics, especially the table ''when to travel'' needs updates and more style
4) This design is very steril, we are looking for clean and modern design
5) On the front page add Company profile text somewhere and add any design on home page is welcome BUT logo must stay where is
6) Please send final print ready documents as well as editable so we can move the logo if needed as it must fit the whole on a brochure holder
7) Last page with contacts very poorly done by my designer, needs upgrade with maybe infographics for phone, email web etc... ideas welcome
8) if you need more photos at the end is link to photo bank

Ideas welcome! Again we need it fast and clean.

Photo bank:
https://files.orvenbox.example/f/q7Lm2Xa9Tz4Pb8Kd

Designes that we linked: https://layoutmarket.example/item/company-profile-square-brochure/48817203?s_rank=8
https://layoutmarket.example/item/company-profile_square/51390628?s_rank=32
https://layoutmarket.example/item/square-brochure/53704916?s_rank=52

This is our webiste so you get the feeling of the colors: www.selvotrips.example

Important: Do not change text, or change pages, everything is as it should be just needs upgradede design! Logo on the first page must stay on the position as is.

Photo bank:

Target Market(s)

We are travel supplier targeting travel agents and travel companies

Industry/Entity Type

Travel Industry

Font styles to use
Serif
Sans Serif

Requirements
Must have
• https://files.orvenbox.example/f/w3Hn6Rc1Ys5Qe2Jv
Nice to have
• Cool design: https://layoutmarket.example/item/business-solution-brochure-template/46182057?s_rank=3
• Cool design 2: https://layoutmarket.example/item/travel-agency-catalog-brochure/47269815?s_rank=6
Should not have
• Do not change the dimensions. You have the design attached, indd file. Needs work and update.

```html
<!DOCTYPE html>
<html lang="en">
<head>
<meta charset="utf-8">
<title>Selvo Trips Croatia – Company Profile</title>
<link rel="stylesheet" href="https://fonts.googleapis.com/css2?family=Montserrat:wght@400;600;700;800&display=swap">
<style>
:root{
  --red:#a3111f;
  --red-deep:#7c0b17;
  --red-dark:#5e0811;
  --paper:#ffffff;
  --stage:#d9d9d9;
}
*{margin:0;padding:0;box-sizing:border-box}
html,body{width:1200px;height:1200px;overflow:hidden}
body{background:var(--stage);font-family:"Montserrat",sans-serif;color:var(--red);position:relative}
.strip{position:absolute;left:62px;background:var(--paper);box-shadow:0 3px 6px rgba(0,0,0,.25);overflow:hidden}
.strip--inside{top:366px;width:1096px;height:219px}
.strip--outside{top:614px;width:1102px;height:220px}
.panel,.photo{position:absolute;top:0;height:100%}
h2{font-weight:800;text-transform:uppercase;line-height:1.15}
.body{font-size:4.2px;line-height:1.5;text-align:justify}
.body p{margin-bottom:4px}
.bullets{list-style:none;font-size:4.2px;line-height:1.45}
.bullets li{margin-bottom:3px}
.corner{position:absolute;background:var(--red)}

/* inside panels */
.intro{left:0;width:132px;padding:16px 14px}
.intro h2{font-size:7px;margin-bottom:7px}
.city-photo{left:132px;width:308px;background:linear-gradient(170deg,#2d79b8 0%,#c9713f 30%,#d98a55 45%,#3a8fb0 62%,#1b5f86 100%)}
.card{position:absolute;background:var(--paper);padding:10px 9px;z-index:2}
.card--group{left:302px;top:27px;width:118px;height:160px;box-shadow:0 1px 3px rgba(0,0,0,.2)}
.card h2{font-size:6.6px;margin-bottom:6px}
.about{left:440px;width:218px;background:linear-gradient(135deg,var(--red) 0%,var(--red-deep) 55%,var(--red-dark) 100%);color:var(--paper);padding:20px 12px}
.about h2{font-size:8px;margin-bottom:7px}
.about .body{width:122px}
.pillars{position:absolute;left:148px;top:52px;width:66px}
.pillar{display:flex;gap:4px;margin-bottom:9px}
.pillar svg{flex:none}
.pillar b{display:block;font-size:3.6px;font-weight:700}
.pillar span{display:block;font-size:3.2px;line-height:1.4}
.yacht-sea{left:658px;width:210px;background:linear-gradient(180deg,#5b93c9 0%,#2e6fa8 45%,#1a4f7a 100%)}
.yacht-sunset{left:774px;width:94px;height:96px!important;background:linear-gradient(180deg,#5a3a3c 0%,#c97a4a 55%,#2c2430 100%)}
.card--yacht{left:670px;top:0;width:104px;height:143px;padding:18px 10px}
.card--yacht h2{font-size:9px;margin-bottom:6px}
.gourmet{left:868px;width:228px}
.cellar{position:absolute;left:8px;top:4px;width:96px;height:70px;background:linear-gradient(135deg,#2b1a12,#8a5a2f 60%,#3b2417)}
.plate{position:absolute;left:8px;top:76px;width:96px;height:143px;background:linear-gradient(160deg,#6b3a24,#d96b3c 45%,#e7b45a 65%,#3a2015)}
.gourmet-text{position:absolute;left:120px;top:26px;width:100px}
.gourmet-text h2{font-size:9px}
.tagline{font-size:4px;margin-bottom:10px}

/* outside panels */
.agents-photo{left:0;width:220px;background:linear-gradient(120deg,#3d86c4 0%,#c8d9e6 45%,#eef1f3 100%)}
.agents-box{position:absolute;left:0;top:132px;width:145px;height:76px;background:var(--red);color:var(--paper);padding:9px 12px}
.agents-box h2{font-size:5px;margin-bottom:4px}
.agents-box .bullets{font-size:3.6px}
.agents-box strong{display:block;font-size:3.8px;font-weight:700;margin-top:4px}
.contact{left:220px;width:221px;text-align:center}
.brand{font-weight:800;letter-spacing:2px;color:var(--red)}
.contact .brand{position:absolute;left:0;right:0;top:108px;font-size:15px}
.contact-lines{position:absolute;left:0;right:0;top:145px;font-size:5px;line-height:1.5}
.contact-lines b{font-weight:800}
.facts{left:441px;width:441px;background:linear-gradient(110deg,#6a8fa6 0%,#a55a45 40%,var(--red) 62%,var(--red-deep) 100%)}
.facts-title{position:absolute;left:15px;top:26px;font-size:13px;font-weight:600;color:#b5202e}
.tiles{position:absolute;left:17px;top:46px;display:grid;grid-template-columns:repeat(3,52px);gap:4px}
.tile{height:52px;background:rgba(163,17,31,.85);border:1px solid rgba(255,255,255,.55);color:var(--paper);display:flex;flex-direction:column;align-items:center;justify-content:flex-end;padding:3px 2px;text-align:center}
.tile svg{margin-bottom:auto;margin-top:5px}
.tile small{font-size:3.2px;line-height:1.3}
.tile b{font-size:5.2px;font-weight:700;line-height:1.15}
.tile--empty{background:none;border:none}
.travel-table{position:absolute;left:243px;top:142px;width:186px;background:rgba(120,10,22,.9);padding:6px;color:var(--paper)}
.table-row{display:grid;grid-template-columns:38px repeat(12,1fr);gap:1.5px;align-items:center;margin-bottom:2px}
.table-row span{font-size:3.4px;font-weight:700}
.month{font-size:3px!important;text-align:center;border:.5px solid rgba(255,255,255,.6)}
.dot{height:9px;border:.5px solid rgba(255,255,255,.6);display:flex;align-items:center;justify-content:center}
.dot::after{content:"";width:5px;height:5px;border-radius:50%;border:.6px solid var(--paper)}
.cover{left:882px;width:220px}
.cover-top{position:absolute;left:0;top:0;width:100%;height:111px;display:flex;align-items:center;justify-content:center}
.cover-top .brand{font-size:17px}
.cover-bottom{position:absolute;left:0;top:111px;width:100%;height:109px;background:linear-gradient(180deg,var(--red),var(--red-deep));text-align:center;color:var(--paper);padding-top:34px}
.cover-bottom h1{font-size:30px;font-weight:800;letter-spacing:1px;color:#e7c6a3}
.cover-bottom p{font-size:6.5px}
</style>
</head>
<body>

<section class="strip strip--inside">
  <div class="panel intro">
    <h2>Customized trips throughout Croatia and Eastern Europe</h2>
    <div class="body">
      <p>We create exceptional customized itineraries via our front line team of local experts, many of whom call Croatia home and are wonderfully experienced in the destinations we sell. Our sales team is constantly living the destinations and receives constant education to stay up to date on products, trends and discoveries, keeping all information at your fingertips.</p>
      <p>Itineraries crafted to perfection according to your clients' interests and preferences. Fast turnaround and guaranteed 48H delivery. Unlimited revisions at no cost. Wide selection of handpicked high-end accommodations including hotels and private villas. Only selling tours that our team has experienced personally. Licensed in-house trained guides for all excursions and transfers. Private transfers and chauffeur service. Combined luxury land and boating itineraries. Shore trips for cruise clients visiting Croatia, Slovenia and Montenegro.</p>
    </div>
  </div>
  <div class="photo city-photo" role="img" aria-label="Aerial view of a walled old town with orange roofs above a blue harbour"></div>
  <div class="card card--group">
    <h2>Small group tours to Croatia and Eastern Europe</h2>
    <div class="body"><p>Work with our team of local destination group experts to develop the finest programs for 10 pax or more. Our group specialists have the experience to create well balanced itineraries and agendas to meet your group's pace and interests.</p></div>
    <ul class="bullets">
      <li>• Exclusive group itineraries designed to meet the way your group travels</li>
      <li>• Special booking conditions for added values, and 1 traveler free on every 15th traveler</li>
      <li>• Group rates available. Use of only high class coaches</li>
      <li>• Combination of land and sea options available</li>
    </ul>
  </div>
  <div class="panel about">
    <h2>About Selvo Trips<br>Croatia</h2>
    <div class="body">
      <p>Since 2003, our team is working specifically on crafting tours that show all the unique experiences in Croatia and beyond, including Montenegro, Serbia, Bosnia and Herzegovina, Greece and Albania. Our company is fully family owned and we offer goes well beyond a travel package; we want all travelers to feel like part of our family. We focus on detailed personalized services for travelers who demand the highest level of service, using carefully selected partners, drivers and guides on each destination.</p>
      <p>Our mission is to always offer exclusive experiences out of the public eye that are preserved for the most discerning travelers to discover the authentic way of life in Croatia and Eastern Europe. We feel that testing and staying on top of new travel trends on the destinations, offering only extraordinary pre-checked activities, is our obligation every day. If you are looking for a partner that will help you provide experiences that can't be found online, we are the right partner for you.</p>
    </div>
    <div class="pillars">
      <div class="pillar"><svg width="16" height="16" viewBox="0 0 16 16"><circle cx="8" cy="8" r="7.4" fill="none" stroke="#fff" stroke-width=".6"/><rect x="5" y="5" width="6" height="6" fill="none" stroke="#fff" stroke-width=".6"/></svg><div><b>RELIABILITY</b><span>Over 15 years of experience with thousands of happy travelers.</span></div></div>
      <div class="pillar"><svg width="16" height="16" viewBox="0 0 16 16"><circle cx="8" cy="8" r="7.4" fill="none" stroke="#fff" stroke-width=".6"/><path d="M5 10l3-4 3 4" fill="none" stroke="#fff" stroke-width=".6"/></svg><div><b>LOCAL EXPERIENCE</b><span>Local know-how that guarantees extraordinary local experience.</span></div></div>
      <div class="pillar"><svg width="16" height="16" viewBox="0 0 16 16"><circle cx="8" cy="8" r="7.4" fill="none" stroke="#fff" stroke-width=".6"/><rect x="5" y="5.5" width="6" height="5" fill="none" stroke="#fff" stroke-width=".6"/></svg><div><b>EXCLUSIVITY</b><span>Access to activities and spots out of public view for selective clients.</span></div></div>
      <div class="pillar"><svg width="16" height="16" viewBox="0 0 16 16"><circle cx="8" cy="8" r="7.4" fill="none" stroke="#fff" stroke-width=".6"/><path d="M6 5v6M10 5v6M6 8h4" stroke="#fff" stroke-width=".6"/></svg><div><b>PERSONAL APPROACH</b><span>Local concierge assigned to every client travelling with us.</span></div></div>
    </div>
  </div>
  <div class="corner" style="left:436px;top:211px;width:8px;height:8px;background:var(--paper)"></div>
  <div class="photo yacht-sea" role="img" aria-label="White motor yacht cruising past a rocky coastline"></div>
  <div class="photo yacht-sunset" role="img" aria-label="Sailboat on the sea at sunset"></div>
  <div class="card card--yacht">
    <h2>Yachting</h2>
    <div class="body"><p>Our yachting department has extensive knowledge of the Adriatic coast and all the destinations on the sea to create the optimal customized routes. Choose between 200,000 vessels in Croatia, available for private explorations of the Adriatic coast and Croatia's 1200 islands.</p></div>
    <ul class="bullets">
      <li>• Pre-checked skippers and crew</li><li>• Customized routes</li><li>• Sailboats</li><li>• Catamarans</li><li>• Gullets</li><li>• Motor yachts</li><li>• Mega yachts</li>
    </ul>
  </div>
  <div class="corner" style="left:766px;top:0;width:8px;height:8px"></div>
  <div class="panel gourmet">
    <div class="cellar" role="img" aria-label="Wine barrels in a cellar"></div>
    <div class="plate" role="img" aria-label="Plate of grilled shrimp with lemon"></div>
    <div class="gourmet-text">
      <h2>Savouria</h2>
      <div class="tagline">The art of Croatian Gourmet</div>
      <div class="body">
        <p>What does it mean to be Savourian? It takes a blend of adventurous minds, creativity and an insider's scoop to the ultimate local gourmet experiences, and fortunately these secret society exists. Launched in 2016, this special department of our company deals with testing and trying local wineries, farms and restaurants to suggest and provide outstanding gourmet daily activities in Croatia. As of now, we included about 20 boutique, family owned wineries and local farms across Croatia that offer incredibly delicious experiences that have no equal. It is always best to immerse and experience the local culture through its food and wine.</p>
        <p>Cooking classes and preparation of local dishes with recognized chefs. Grape harvests and award winning wines. Olive oil preparation and tasting.</p>
      </div>
    </div>
    <div class="corner" style="left:220px;top:0;width:8px;height:40px"></div>
  </div>
  <div class="corner" style="left:0;top:0;width:3px;height:219px"></div>
  <div class="corner" style="left:124px;top:211px;width:8px;height:8px"></div>
</section>

<section class="strip strip--outside">
  <div class="photo agents-photo" role="img" aria-label="Travel agent with a headset working beside a desk globe"></div>
  <div class="agents-box">
    <h2>Travel agents, what's in it for you?</h2>
    <ul class="bullets">
      <li>• We work exclusively with travel agents, we don't market or sell directly to the public</li>
      <li>• High paying commission up to 15%</li>
      <li>• Incentive programs available</li>
      <li>• Travel agent support and fast itinerary turnaround</li>
    </ul>
    <strong>We are your strongest local link in Croatia and Eastern Europe!</strong>
  </div>
  <div class="panel contact">
    <div class="brand">SELVO TRIPS</div>
    <div class="contact-lines">
      <b>SELVO TRIPS CROATIA</b><br>
      A: 88 Harbor Lane, Millbrook, OH, 45000<br>
      TollFree +1 800 555 0142<br>
      Direct +1 216 555 0187<br>
      e-mail: sales@selvotrips.example<br>
      web: www.selvotrips.example
    </div>
  </div>
  <div class="panel facts" role="img" aria-label="Croatian coastal fortress and old town with a red map silhouette of Croatia"></div>
  <div class="panel" style="left:441px;width:441px">
    <h2 class="facts-title">Croatia</h2>
    <div class="tiles">
      <div class="tile"><svg width="22" height="16" viewBox="0 0 22 16"><path d="M1 1h20v10H8l-4 4v-4H1z" fill="none" stroke="#fff" stroke-width=".8"/></svg><b>LANGUAGE</b></div>
      <div class="tile"><svg width="24" height="14" viewBox="0 0 24 14"><g fill="#fff"><circle cx="4" cy="3" r="2"/><circle cx="10" cy="3" r="2"/><circle cx="16" cy="3" r="2"/><circle cx="22" cy="3" r="2"/><rect x="2" y="6" width="4" height="7"/><rect x="8" y="6" width="4" height="7"/><rect x="14" y="6" width="4" height="7"/><rect x="20" y="6" width="4" height="7"/></g></svg><small>4.284 MILLION</small><b>POPULATION</b></div>
      <div class="tile tile--empty"></div>
      <div class="tile"><svg width="14" height="16" viewBox="0 0 14 16"><g fill="none" stroke="#fff" stroke-width=".8"><ellipse cx="7" cy="3" rx="6" ry="2"/><path d="M1 3v10c0 1 3 2 6 2s6-1 6-2V3"/></g></svg><small>KUNA (HRK)</small><b>CURRENCY</b></div>
      <div class="tile"><svg width="20" height="16" viewBox="0 0 20 16"><g fill="none" stroke="#fff" stroke-width=".8"><path d="M1 5l9-4 9 4z"/><path d="M3 6v8M7 6v8M13 6v8M17 6v8M1 15h18"/></g></svg><small>8 PROPERTIES ON THE HERITAGE LIST</small><b>UNESCO</b></div>
      <div class="tile tile--empty"></div>
      <div class="tile"><svg width="14" height="18" viewBox="0 0 14 18"><g fill="none" stroke="#fff" stroke-width=".8"><path d="M7 1v4M5 3h4M2 17V9l5-4 5 4v8z"/></g></svg><b>CATHOLIC<br>RELIGION</b></div>
      <div class="tile"><svg width="20" height="16" viewBox="0 0 20 16"><g fill="none" stroke="#fff" stroke-width=".8"><circle cx="6" cy="5" r="4"/><circle cx="14" cy="5" r="4"/><path d="M1 12h18M3 15h14"/></g></svg><small>8 SPECTACULAR NATIONAL PARKS</small><b>NATIONAL PARKS</b></div>
      <div class="tile"><svg width="30" height="14" viewBox="0 0 30 14"><path d="M1 8l10-2 4-5h2l-2 5 8-1 2-2h2l-1 4 1 4h-2l-2-2-8-1 2 5h-2l-4-5z" fill="#fff"/></svg><small>ZAGREB · PULA · ZADAR · SPLIT · DUBROVNIK</small><b>AIRPORTS</b></div>
    </div>
    <svg style="position:absolute;left:344px;top:38px" width="16" height="20" viewBox="0 0 16 20"><path d="M8 19C3 12 1 9 1 7a7 7 0 0114 0c0 2-2 5-7 12z" fill="#fff"/><circle cx="8" cy="7" r="3.5" fill="#a3111f"/></svg>
    <div class="travel-table">
      <div class="table-row"><span>WHEN TO GO?</span><span class="month">JAN</span><span class="month">FEB</span><span class="month">MAR</span><span class="month">APR</span><span class="month">MAY</span><span class="month">JUN</span><span class="month">JUL</span><span class="month">AUG</span><span class="month">SEP</span><span class="month">OCT</span><span class="month">NOV</span><span class="month">DEC</span></div>
      <div class="table-row"><span>WEATHER</span><i class="dot"></i><i class="dot"></i><i class="dot"></i><i class="dot"></i><i class="dot"></i><i class="dot"></i><i class="dot"></i><i class="dot"></i><i class="dot"></i><i class="dot"></i><i class="dot"></i><i class="dot"></i></div>
      <div class="table-row"><span>CROWDS</span><i class="dot"></i><i class="dot"></i><i class="dot"></i><i class="dot"></i><i class="dot"></i><i class="dot"></i><i class="dot"></i><i class="dot"></i><i class="dot"></i><i class="dot"></i><i class="dot"></i><i class="dot"></i></div>
      <div class="table-row"><span>PRICES</span><i class="dot"></i><i class="dot"></i><i class="dot"></i><i class="dot"></i><i class="dot"></i><i class="dot"></i><i class="dot"></i><i class="dot"></i><i class="dot"></i><i class="dot"></i><i class="dot"></i><i class="dot"></i></div>
    </div>
  </div>
  <div class="panel cover">
    <div class="cover-top"><div class="brand">SELVO TRIPS</div></div>
    <div class="cover-bottom" role="img" aria-label="Faded view of an old town skyline behind the title">
      <h1>CROATIA</h1>
      <p>We Live it. You'll Love it.</p>
    </div>
  </div>
</section>

</body>
</html>
```